New Joomla Website for Marquee Hire Co

We need a web design for our new Marquee Hire Co here in New Zealand called Brightfield Canopies.
We rather like the retro look, as it fit very well with the current trends in weddings that is a more of a retro look (and we had our logo designed to reflect that!). The 50's and 60's wedding styles are really making a comeback. We would like to communicate to that market effectively.

The Home page should have a slider image with space for a headline on it. It is a visual product we have (but we are selling that dream of a perfect wedding/party/event).

Our competition here have a really nice site that you could look at - www.plovane.co.nz

The other pages would have space for a picture, and then a blurb under each element related to it.
We will have a FAQ, Gallery, Hire and Contact us pages - we will add them as we go along.

From a technical perspective, we are using Joomla 2.5 and upwards.

Any questions - let me know. I look forward seeing the designs!

Target Market(s)

Couples looking for a wedding marquee, birthday parties, Corporate events

Industry/Entity Type

Wedding

Requirements
Must have
• 1. Preferably done in Joomla. I will also look at Wordpress site.
2. It has to have a retro look and feel.
3. It has to use my brand new logo (included)

```html
<!DOCTYPE html>
<html lang="en">
<head>
<meta charset="utf-8">
<title>Brightfield Canopies – Marquee Hire New Zealand</title>
<link rel="stylesheet" href="https://fonts.googleapis.com/css2?family=Arimo:ital,wght@0,400;1,400&family=Londrina+Solid:wght@400&family=Roboto+Condensed:wght@400&display=swap">
<style>
  :root{
    --header-brown:#3b2a1f;
    --header-top:#6b4f34;
    --ribbon:#6e5540;
    --ribbon-dark:#4b3829;
    --nav-text:#efe3cf;
    --call-red:#d6512b;
    --cream:#f0dcae;
    --cream-light:#f6e8c8;
    --panel:#faf6ee;
    --panel-border:#e3cfa3;
    --dash:#e2c68e;
    --ink:#3a2a20;
    --caption-ink:#1b1410;
    --body-text:#666058;
    --accent-brown:#7a3a0e;
    --dark-panel:#35251b;
    --light-text:#f4efe6;
    --footer:#d9c9a6;
    --footer-text:#3b2b20;
  }
  *{box-sizing:border-box;margin:0;padding:0}
  html,body{width:1175px;height:1200px;overflow:hidden}
  body{position:relative;background:linear-gradient(180deg,var(--cream-light) 0%,var(--cream) 60%,#ecd6a4 100%);font-family:"Arimo",Arial,sans-serif;color:var(--ink)}
  .abs{position:absolute}

  /* header */
  .site-header{left:0;top:0;width:1175px;height:190px;background:var(--header-brown);border-top:7px solid var(--header-top)}
  .header-edge{left:0;top:188px;width:1175px;height:10px}
  .social{left:127px;top:32px;display:flex;gap:8px}
  .social span{width:32px;height:32px;border-radius:50%;background:#8a6a4e;display:block;border:2px solid #a78564}
  .call{right:125px;top:34px;font-family:"Londrina Solid",sans-serif;font-size:23px;color:var(--call-red);letter-spacing:.5px}
  .ribbon-tail{top:105px;width:80px;height:50px;background:var(--ribbon-dark)}
  .ribbon-tail.left{left:118px;clip-path:polygon(0 0,100% 0,100% 100%,0 100%,14% 50%)}
  .ribbon-tail.right{left:978px;clip-path:polygon(0 0,100% 0,86% 50%,100% 100%,0 100%)}
  .main-nav{left:165px;top:93px;width:848px;height:49px;background:var(--ribbon);box-shadow:0 3px 6px rgba(0,0,0,.35)}
  .main-nav a{position:absolute;top:13px;font-family:"Londrina Solid",sans-serif;font-size:18px;color:var(--nav-text);text-decoration:none;letter-spacing:1px}
  .brand{left:480px;top:104px;width:218px;display:flex;align-items:center;justify-content:center;gap:8px;font-family:"Londrina Solid",sans-serif;font-size:22px;color:var(--nav-text);letter-spacing:.5px;white-space:nowrap}
  .brand .dot{width:12px;height:12px;border-radius:50%;background:var(--nav-text);display:block}

  /* decorative florals */
  .floral{top:196px;width:125px;height:420px;background:radial-gradient(ellipse at 40% 50%,#f3cf7e 0%,#e9c17d 35%,rgba(233,193,125,0) 75%)}
  .floral.left{left:0}
  .floral.right{right:0}

  /* slider */
  .slider{left:118px;top:220px;width:940px;height:391px;background:#fff;box-shadow:0 8px 14px rgba(80,50,20,.25)}
  .slide-photo{left:9px;top:11px;width:921px;height:369px;background:linear-gradient(180deg,#3f5a2c 0%,#6e8b4a 16%,#eef0ee 30%,#dfe2e2 60%,#8a7a6a 80%,#6a5442 100%)}
  .caption{left:157px;top:334px;width:412px;height:171px;background:rgba(255,255,255,.55);border:1px solid #6b5f55;padding:20px 8px 0 8px}
  .caption h1{font-family:"Londrina Solid",sans-serif;font-weight:400;font-size:40px;color:var(--caption-ink);letter-spacing:1px;line-height:1}
  .caption p{margin-top:22px;font-size:14px;line-height:17px;text-align:justify;color:#222}
  .arrow{top:386px;width:60px;height:60px;border-radius:50%;background:#f1f1f1;box-shadow:0 2px 4px rgba(0,0,0,.35)}
  .arrow.prev{left:78px}.arrow.next{left:1038px}
  .arrow svg{position:absolute;left:15px;top:15px}
  .dots{left:550px;top:636px;display:flex;gap:6px}
  .dots span{width:10px;height:10px;border-radius:50%;background:#5d5650;box-shadow:inset 0 1px 1px #000}
  .dots span.on{background:#f6f1e6}

  /* content boxes */
  .box{top:684px;width:293px;height:245px;background:var(--panel);border:1px solid var(--panel-border);padding:0 8px}
  .box h2{font-family:"Roboto Condensed",sans-serif;font-weight:400;font-size:21px;color:var(--ink);padding:15px 0 10px;border-bottom:1px dashed var(--dash)}
  .box .lead{font-style:italic;font-size:12.5px;color:var(--accent-brown);margin:11px 0 0 6px}
  .box p.copy{font-size:11.3px;line-height:14.3px;color:var(--body-text);text-align:justify;margin-top:12px;padding:0 4px}
  .box .media{margin-top:8px;width:275px;height:176px;position:relative}
  .video-photo{background:radial-gradient(ellipse at 50% 75%,#e9ddd2 0%,#bfae9f 35%,#3f3430 80%)}
  .gallery-photo{background:radial-gradient(ellipse at 50% 40%,#efe0cc 0%,#b7906a 40%,#4a3426 85%)}
  .play{left:110px;top:70px;width:62px;height:42px;border-radius:8px;background:rgba(40,40,40,.75)}
  .mini-arrow{top:74px;width:22px;height:22px;border-radius:50%;background:rgba(30,30,30,.6)}

  /* dark panels */
  .dark{top:950px;height:142px;background:var(--dark-panel);border-radius:3px;box-shadow:0 2px 5px rgba(0,0,0,.3);color:#f2ece3}
  .offers{left:118px;width:617px}
  .offers h2{position:absolute;left:15px;top:14px;font-family:"Londrina Solid",sans-serif;font-weight:400;font-size:38px;color:var(--light-text);letter-spacing:1px;line-height:1}
  .offers p{position:absolute;left:15px;top:68px;width:366px;font-size:11.3px;line-height:14.4px}
  .read-more{left:15px;top:116px;font-family:"Londrina Solid",sans-serif;font-size:12px;color:#f2ece3;display:flex;align-items:center;gap:5px}
  .offers-photo{left:393px;top:9px;width:220px;height:124px;border-radius:5px;border:1px solid #c9b9a2;background:radial-gradient(ellipse at 40% 40%,#fff5ef 0%,#e9c6bd 35%,#b53a33 70%,#6d2a22 100%)}
  .testimonials{left:765px;width:293px}
  .testimonials h2{position:absolute;left:9px;top:10px;font-family:"Londrina Solid",sans-serif;font-weight:400;font-size:21px;color:var(--light-text);letter-spacing:1px;line-height:1}
  .testimonials p{position:absolute;left:11px;top:48px;width:272px;font-style:italic;font-size:11.3px;line-height:16.6px;text-align:justify}
  .testimonials .by{position:absolute;right:12px;top:113px;font-family:"Londrina Solid",sans-serif;font-size:17px;letter-spacing:1px}

  /* footer */
  .site-footer{left:0;top:1114px;width:1175px;height:86px;background:var(--footer);font-size:12.5px;color:var(--footer-text)}
  .site-footer .copy{position:absolute;left:117px;top:43px}
  .site-footer .links{position:absolute;left:831px;top:43px}
  .site-footer .code{position:absolute;left:1135px;top:43px}
</style>
</head>
<body>

<header class="site-header abs">
  <div class="social abs" aria-label="Social links">
    <span></span><span></span><span></span><span></span><span></span><span></span>
  </div>
  <div class="call abs">CALL US : (000) 000 0000</div>
</header>
<svg class="header-edge abs" width="1175" height="10" viewBox="0 0 1175 10" preserveAspectRatio="none">
  <defs><pattern id="zig" width="8" height="10" patternUnits="userSpaceOnUse"><path d="M0 0H8V3L4 8L0 3Z" fill="#3b2a1f"/></pattern></defs>
  <rect width="1175" height="10" fill="url(#zig)"/>
</svg>

<div class="ribbon-tail left abs"></div>
<div class="ribbon-tail right abs"></div>
<nav class="main-nav abs">
  <a style="left:33px">HOME</a>
  <a style="left:127px">FAQ</a>
  <a style="left:222px">HIRE</a>
  <a style="left:605px">GALLERY</a>
  <a style="left:720px">CONTACT US</a>
</nav>
<div class="brand abs"><span class="dot"></span>Brightfield Canopies</div>

<div class="floral left abs" role="img" aria-label="Yellow hand-drawn flower decoration"></div>
<div class="floral right abs" role="img" aria-label="Yellow hand-drawn flower decoration"></div>

<section class="slider abs">
  <div class="slide-photo abs" role="img" aria-label="White stretch marquee in a garden with wedding guests"></div>
</section>
<div class="caption abs">
  <h1>Brightfield Canopies</h1>
  <p>Smnis iste natus error sit voluptatem accusantium doloremque laudantium, totam rem aperiam, eaque ipsa quae ab illo inventore veritatis et quasi architecto beatae vitae dicta sunt explicabo.</p>
</div>
<div class="arrow prev abs"><svg width="30" height="30" viewBox="0 0 30 30"><path d="M24 4L5 15L24 26Z" fill="#2b2b2b"/></svg></div>
<div class="arrow next abs"><svg width="30" height="30" viewBox="0 0 30 30"><path d="M6 4L25 15L6 26Z" fill="#2b2b2b"/></svg></div>
<div class="dots abs"><span></span><span class="on"></span><span></span><span></span><span></span></div>

<section class="box abs" style="left:117px">
  <h2>What We Do!</h2>
  <p class="lead">So accusantium doloremque laudantium,</p>
  <p class="copy">totam rem aperiam, eaque ipsa quae ab illo inventore veritatis et quasi architecto beatae vitae dicta sunt explicabo.</p>
  <p class="copy">Nemo enim ipsam voluptatem quia voluptas sit aspernatur aut odit aut fugit, sed quia consequuntur magni dolores eos qui ratione voluptatem sequi nesciunt. Neque porro quisquam est, qui dolorem ipsum quia dolor sit amet, consectetur,ipsum quia dolor sit amet, consectetur, adipisci velit</p>
</section>
<section class="box abs" style="left:439px">
  <h2>Our Videos</h2>
  <div class="media video-photo" role="img" aria-label="Banquet tables set for a wedding reception">
    <div class="play abs"><svg width="62" height="42" viewBox="0 0 62 42"><path d="M25 11L40 21L25 31Z" fill="#e8e8e8"/></svg></div>
  </div>
</section>
<section class="box abs" style="left:762px">
  <h2>Our Gallery</h2>
  <div class="media gallery-photo" role="img" aria-label="Reception hall with floral centrepieces">
    <div class="mini-arrow abs" style="left:4px"><svg width="22" height="22" viewBox="0 0 22 22"><path d="M13 6L8 11L13 16" stroke="#fff" stroke-width="2" fill="none"/></svg></div>
    <div class="mini-arrow abs" style="right:4px"><svg width="22" height="22" viewBox="0 0 22 22"><path d="M9 6L14 11L9 16" stroke="#fff" stroke-width="2" fill="none"/></svg></div>
  </div>
</section>

<section class="dark offers abs">
  <h2>SPECIAL OFFERS</h2>
  <p>Nemo enim ipsam voluptatem quia voluptas sit aspernatur aut odit aut fugit, sed quia consequuntur magni dolores eos qui ratNemo enim ipsam voluptatem quia voluptas..</p>
  <div class="read-more abs">READ MORE <svg width="16" height="12" viewBox="0 0 16 12"><path d="M1 6H13M8 1L14 6L8 11" stroke="#e9dcc4" stroke-width="2.4" fill="none"/></svg></div>
  <div class="offers-photo abs" role="img" aria-label="Table setting with red glasses and rose petals"></div>
</section>
<section class="dark testimonials abs">
  <h2>TESTIMONIALS</h2>
  <p>Nemo enim ipsam voluptatem quia voluptas sit aspernatur aut odit aut fugit, sed quia consequuntur maspernatur aut odit sed quia consequuntur m<br>Thanks</p>
  <div class="by">HARLOW</div>
</section>

<footer class="site-footer abs">
  <span class="copy">© 2012 Brightfield Canopies. All rights reserved.</span>
  <span class="links">Privacu Policy &nbsp;|&nbsp; Terms of use| Sitemap</span>
  <span class="code">C2</span>
</footer>

</body>
</html>
```